QRV In Home Flier

To prepare a flier to be placed directly into existing clients homes, which shares additional services available. These are clients that are using QRV Cleaning services and we want to use our QRV Pest Control or BWO (Bondo Mend Up)Maintenance Services

Target Market(s)

residential home owners / Renters

Industry/Entity Type

Property Maintenance

Colors

Designer to choose colors to be used in the design.

Requirements
Must have
• Must be crisp and clean - design should pop - A CLEAR call to action
Nice to have
• See previous designed uploaded
Should not have

```html
<!DOCTYPE html>
<html lang="en">
<head>
<meta charset="utf-8">
<title>QRV Pest Control Flier</title>
<link rel="stylesheet" href="https://fonts.googleapis.com/css2?family=Montserrat:wght@300;400;500;600;700;800&display=swap">
<style>
  :root {
    --brand-blue: #1466b8;
    --brand-blue-dark: #0f4f93;
    --accent-orange: #e8921f;
    --ink: #4a4a52;
    --ink-soft: #6b6b73;
    --band-grey: #e6e6e8;
    --paper: #ffffff;
  }
  * { margin: 0; padding: 0; box-sizing: border-box; }
  html, body { width: 800px; height: 1200px; overflow: hidden; background: var(--paper); }
  body { font-family: "Montserrat", sans-serif; color: var(--ink); }
  .flier { position: relative; width: 800px; height: 1200px; overflow: hidden; background: var(--paper); }
  .flier-shapes { position: absolute; inset: 0; }
  .brand { position: absolute; left: 50px; top: 86px; display: flex; align-items: center; gap: 12px; }
  .brand-dot { width: 44px; height: 44px; border-radius: 50%; background: var(--brand-blue); }
  .brand-name { font-weight: 700; font-size: 22px; color: var(--brand-blue); }
  .hero-title { position: absolute; left: 455px; top: 222px; color: #fff; }
  .hero-title .word-main { display: block; font-weight: 800; font-size: 74px; line-height: 1; letter-spacing: 1px; }
  .hero-title .word-light { display: block; font-weight: 300; font-size: 50px; line-height: 1.15; letter-spacing: 1px; }
  .hero-points { position: absolute; left: 458px; top: 456px; color: #fff; font-size: 15px; font-weight: 600; line-height: 1.4; }
  .offer-badge { position: absolute; left: 560px; top: 772px; width: 196px; height: 196px; display: flex; align-items: center; justify-content: center; text-align: center; color: #1b1b1b; font-weight: 700; font-size: 24px; line-height: 1.2; }
  .services { position: absolute; left: 62px; top: 782px; display: grid; grid-template-columns: 196px 192px 150px; row-gap: 40px; list-style: none; }
  .service { display: flex; align-items: center; gap: 12px; font-size: 12px; font-weight: 500; line-height: 1.25; color: var(--ink-soft); }
  .service-icon { width: 44px; height: 44px; flex: none; }
  .about { position: absolute; left: 48px; top: 968px; width: 400px; }
  .about-lead { font-size: 17px; font-weight: 500; line-height: 1.35; color: var(--ink); }
  .about-body { margin-top: 18px; font-size: 14px; line-height: 1.35; text-align: justify; color: var(--ink-soft); font-weight: 500; }
  .website { position: absolute; left: 48px; top: 1132px; display: flex; align-items: center; gap: 20px; font-size: 19px; font-weight: 600; color: var(--ink); }
  .website-icon { width: 22px; height: 22px; }
  .call-to-action { position: absolute; left: 545px; top: 990px; width: 230px; text-align: center; color: #fff; font-weight: 600; }
  .cta-lead { font-size: 19px; line-height: 1.25; }
  .cta-vanity { font-size: 31px; font-weight: 700; line-height: 1.3; }
  .cta-phone { font-size: 19px; line-height: 1.6; }
</style>
</head>
<body>
<main class="flier">
  <svg class="flier-shapes" width="800" height="1200" viewBox="0 0 800 1200">
    <defs>
      <linearGradient id="heroPhotoTone" x1="0" y1="0" x2="1" y2="1">
        <stop offset="0" stop-color="#f3f5f8"/>
        <stop offset="0.5" stop-color="#cfd7e0"/>
        <stop offset="1" stop-color="#9ea9b6"/>
      </linearGradient>
      <linearGradient id="heroFadeLeft" x1="0" y1="0" x2="1" y2="0">
        <stop offset="0" stop-color="#fff" stop-opacity="0.85"/>
        <stop offset="0.35" stop-color="#fff" stop-opacity="0"/>
      </linearGradient>
      <linearGradient id="heroFadeBottom" x1="0" y1="0" x2="0" y2="1">
        <stop offset="0.7" stop-color="#fff" stop-opacity="0"/>
        <stop offset="1" stop-color="#fff" stop-opacity="1"/>
      </linearGradient>
      <linearGradient id="thumbTone" x1="0" y1="0" x2="1" y2="1">
        <stop offset="0" stop-color="#e5e1d6"/>
        <stop offset="1" stop-color="#8c7f66"/>
      </linearGradient>
    </defs>

    <g role="img" aria-label="Photo of a technician in a white protective suit and mask spraying along a kitchen counter">
      <rect x="0" y="0" width="800" height="620" fill="url(#heroPhotoTone)"/>
      <rect x="0" y="0" width="800" height="620" fill="url(#heroFadeLeft)"/>
      <rect x="0" y="0" width="800" height="620" fill="url(#heroFadeBottom)"/>
    </g>
    <path d="M0 560 Q200 640 420 600 Q600 570 800 640 L800 1200 L0 1200 Z" fill="var(--paper)"/>

    <circle cx="605" cy="360" r="232" fill="var(--brand-blue)" opacity="0.96"/>

    <circle cx="138" cy="593" r="90" fill="#fff"/>
    <circle cx="138" cy="593" r="84" fill="url(#thumbTone)" role="img" aria-label="Photo of a technician treating a wooden floor edge"/>
    <circle cx="322" cy="590" r="88" fill="#fff"/>
    <circle cx="322" cy="590" r="82" fill="url(#thumbTone)" role="img" aria-label="Photo of a sprayer applied to an exterior wall base"/>
    <circle cx="548" cy="740" r="88" fill="#fff"/>
    <circle cx="548" cy="740" r="82" fill="url(#thumbTone)" role="img" aria-label="Photo of a technician spraying a kitchen cabinet"/>

    <rect x="0" y="1140" width="800" height="60" fill="var(--band-grey)"/>
    <circle cx="790" cy="1255" r="384" fill="var(--paper)"/>
    <circle cx="790" cy="1255" r="370" fill="var(--brand-blue)"/>

    <circle cx="658" cy="870" r="104" fill="#fff"/>
    <circle cx="658" cy="870" r="98" fill="var(--accent-orange)"/>
  </svg>

  <div class="brand">
    <span class="brand-dot"></span>
    <span class="brand-name">QRV Pest Control</span>
  </div>

  <h1 class="hero-title">
    <span class="word-main">PEST</span>
    <span class="word-light">CONTROL</span>
    <span class="word-light">SERVICE</span>
  </h1>
  <p class="hero-points">
    European managed<br>
    MONTHLY - QUARTERLY - ANNUALLY<br>
    maintenance contracts<br>
    On call service<br>
    Your property, our priority.
  </p>

  <div class="offer-badge">SPECIAL<br>INCENTIVE<br>FOR QRV<br>CLIENT</div>

  <ul class="services">
    <li class="service"><svg class="service-icon" viewBox="0 0 44 44"><circle cx="22" cy="22" r="20" fill="none" stroke="#555" stroke-width="2"/><circle cx="22" cy="22" r="7" fill="#555"/></svg><span>General Pest<br>Control</span></li>
    <li class="service"><svg class="service-icon" viewBox="0 0 44 44"><circle cx="22" cy="22" r="20" fill="none" stroke="#555" stroke-width="2"/><circle cx="22" cy="22" r="7" fill="#555"/></svg><span>Bed Bugs<br>Control</span></li>
    <li class="service" style="visibility:hidden"><span></span></li>
    <li class="service"><svg class="service-icon" viewBox="0 0 44 44"><circle cx="22" cy="22" r="20" fill="none" stroke="#555" stroke-width="2"/><line x1="9" y1="35" x2="35" y2="9" stroke="#555" stroke-width="2"/></svg><span>Cockroaches<br>Control</span></li>
    <li class="service"><svg class="service-icon" viewBox="0 0 44 44"><circle cx="22" cy="22" r="20" fill="none" stroke="#555" stroke-width="2"/><circle cx="22" cy="22" r="7" fill="#555"/></svg><span>Rat<br>Control</span></li>
    <li class="service"><svg class="service-icon" viewBox="0 0 44 44"><circle cx="22" cy="22" r="20" fill="none" stroke="#555" stroke-width="2"/><line x1="9" y1="35" x2="35" y2="9" stroke="#555" stroke-width="2"/></svg><span>Ant<br>Control</span></li>
  </ul>

  <section class="about">
    <p class="about-lead">QRV Pest Control is reinventing the pest control service industry in Dubai.</p>
    <p class="about-body">This means you get the right Pest Control Workers, with the right tools at the right time!</p>
  </section>

  <div class="website">
    <svg class="website-icon" viewBox="0 0 22 22"><circle cx="11" cy="11" r="10" fill="#222"/><ellipse cx="11" cy="11" rx="4" ry="10" fill="none" stroke="#fff" stroke-width="1.2"/><line x1="1" y1="11" x2="21" y2="11" stroke="#fff" stroke-width="1.2"/></svg>
    <span>www.qrvhomecare.com</span>
  </div>

  <div class="call-to-action">
    <p class="cta-lead">Call us now for a<br>FREE ESTIMATE!</p>
    <p class="cta-vanity">800 Homely</p>
    <p class="cta-phone">+971 04 555 0172<br>+971 56 555 0938</p>
  </div>
</main>
</body>
</html>
```